Business Card for Field Lotus-Eco Friendly Organic Clothing Brand

We are looking for an amazing business card for our eco friendly, organic clothing brand. We are thinking maybe a business card with a peel off sticker on the back, since our hanging clothing tag is a peel off sticker on the back. I will attach our hang tag so we can make sure we stay in line with our design. I've also attached a bag we are doing because I do like the scattered emblem look as well.

```html
<!DOCTYPE html>
<html lang="en">
<head>
<meta charset="utf-8">
<title>Field Lotus – Business Card</title>
<link href="https://fonts.googleapis.com/css2?family=Exo+2:wght@600;700&family=Noto+Sans:wght@400;500&display=swap" rel="stylesheet">
<style>
  :root {
    --stage: #2a2a2c;
    --card-dark: #1c1f24;
    --card-olive: #26271f;
    --gold: #d9a52a;
    --gold-light: #f2cf63;
    --gold-deep: #a87818;
  }
  * { box-sizing: border-box; margin: 0; padding: 0; }
  html, body { width: 1200px; height: 1189px; overflow: hidden; }
  body {
    background: var(--stage);
    position: relative;
    font-family: "Noto Sans", sans-serif;
  }
  .card {
    position: absolute;
    left: 170px;
    width: 860px;
    height: 490px;
    border-radius: 26px;
    overflow: hidden;
  }
  /* Front */
  .card--front { top: 70px; background: var(--card-olive); }
  .front-pattern {
    position: absolute; inset: 0;
    background:
      radial-gradient(circle at 20% 30%, rgba(217,165,42,.28), transparent 40%),
      radial-gradient(circle at 80% 25%, rgba(217,165,42,.24), transparent 38%),
      radial-gradient(circle at 30% 80%, rgba(217,165,42,.22), transparent 40%),
      radial-gradient(circle at 75% 78%, rgba(217,165,42,.26), transparent 38%),
      var(--card-olive);
  }
  .brand-frame {
    position: absolute;
    left: 120px; top: 175px;
    width: 620px; height: 140px;
    border: 4px solid var(--gold);
    background: var(--card-olive);
    display: flex; align-items: center; justify-content: center;
  }
  .brand-frame__name {
    font-family: "Exo 2", sans-serif;
    font-weight: 700;
    font-size: 84px;
    letter-spacing: 2px;
    color: var(--gold);
  }
  /* Back */
  .card--back { top: 630px; background: var(--card-dark); }
  .logo {
    position: absolute; left: 48px; top: 44px;
    display: flex; align-items: center; gap: 18px;
  }
  .logo__square { width: 70px; height: 70px; background: var(--gold); }
  .logo__name {
    font-family: "Exo 2", sans-serif; font-weight: 700;
    font-size: 42px; color: var(--gold);
  }
  .logo__url {
    position: absolute; left: 136px; top: 122px;
    font-size: 15px; color: var(--gold);
  }
  .person {
    position: absolute; right: 60px; top: 150px; text-align: right;
    color: var(--gold);
  }
  .person__name {
    font-family: "Exo 2", sans-serif; font-weight: 700; font-size: 36px;
    letter-spacing: 1px;
  }
  .person__role { font-size: 22px; margin-top: -4px; }
  .divider {
    position: absolute; left: 48px; right: 60px; top: 250px;
    height: 2px; background: var(--gold);
  }
  .contact {
    position: absolute; left: 48px; top: 300px;
    list-style: none; display: flex; flex-direction: column; gap: 14px;
  }
  .contact__item {
    display: flex; align-items: center; gap: 18px;
    font-size: 28px; color: var(--gold);
  }
  .contact__icon {
    width: 34px; height: 34px; border-radius: 4px;
    background: linear-gradient(135deg, var(--gold-light), var(--gold-deep));
    display: flex; align-items: center; justify-content: center;
  }
  .address {
    position: absolute; right: 60px; top: 285px; text-align: right;
    font-style: normal;
    font-size: 26px; line-height: 1.3; color: var(--gold);
  }
</style>
</head>
<body>
  <section class="card card--front">
    <div class="front-pattern" role="img" aria-label="Gold decorative pattern on dark olive"></div>
    <div class="brand-frame"><span class="brand-frame__name">Field Lotus</span></div>
  </section>

  <section class="card card--back">
    <div class="logo">
      <span class="logo__square"></span>
      <span class="logo__name">Field Lotus</span>
    </div>
    <span class="logo__url">www.fieldlotus.com</span>

    <div class="person">
      <div class="person__name">Employee Name</div>
      <div class="person__role">Manager</div>
    </div>

    <div class="divider"></div>

    <ul class="contact">
      <li class="contact__item">
        <span class="contact__icon">
          <svg width="20" height="20" viewBox="0 0 24 24"><path d="M6.6 10.8a15 15 0 0 0 6.6 6.6l2.2-2.2a1 1 0 0 1 1-.25 11.4 11.4 0 0 0 3.6.57 1 1 0 0 1 1 1V20a1 1 0 0 1-1 1A17 17 0 0 1 3 4a1 1 0 0 1 1-1h3.5a1 1 0 0 1 1 1c0 1.25.2 2.45.57 3.57a1 1 0 0 1-.25 1z" fill="#1c1f24"/></svg>
        </span>0123 456 789
      </li>
      <li class="contact__item">
        <span class="contact__icon">
          <svg width="22" height="16" viewBox="0 0 22 16"><rect x="1" y="1" width="20" height="14" fill="none" stroke="#1c1f24" stroke-width="2"/><path d="M1 1l10 8 10-8" fill="none" stroke="#1c1f24" stroke-width="2"/></svg>
        </span>your@yourgmail.net.nz
      </li>
      <li class="contact__item">
        <span class="contact__icon">
          <svg width="22" height="22" viewBox="0 0 22 22"><circle cx="11" cy="11" r="9" fill="none" stroke="#1c1f24" stroke-width="2"/><ellipse cx="11" cy="11" rx="4" ry="9" fill="none" stroke="#1c1f24" stroke-width="1.6"/><path d="M2 11h18" stroke="#1c1f24" stroke-width="1.6"/></svg>
        </span>www.yourwebsite.co.nz
      </li>
    </ul>

    <address class="address">your address 2nd street<br>london USA</address>
  </section>
</body>
</html>
```